Visitenkarten mit schwarzem Design gesucht
Zielgruppe
Zielgruppe sind Feinschmecker & Genießer.
Aufgabenstellung
Front schwarz mit unserem goldenen Logo. Rückseite auch in schwarz mit Firmenname, Adresse, Telefon, Email und Webadresse.
Es wäre klasse, wenn nach Beendigung des Projektes Datei für drei Ansprechpartner zur Verfügung gestellt werden. Das heißt, drei verschiedene Namen und Telefonnummern. Der Rest wäre dann gleichbleibend.
Bei der Gestaltung bitte bei der .eps Datei nur das Logo verwenden und nicht den Text!

```html
<!DOCTYPE html>
<html lang="de">
<head>
<meta charset="utf-8">
<title>Visitenkarte – Aurelia Tafel</title>
<link rel="stylesheet" href="https://fonts.googleapis.com/css2?family=Source+Sans+3:wght@400;600&display=swap">
<style>
  :root {
    --backdrop: #c4c4c4;
    --card-black: #121212;
    --gold: #c9a243;
    --gold-light: #e3c46e;
    --gold-dark: #9c7a2a;
  }
  html, body {
    margin: 0;
    padding: 0;
    width: 1200px;
    height: 1200px;
    overflow: hidden;
    background: var(--backdrop);
  }
  .sheet {
    width: 1200px;
    height: 1200px;
    display: flex;
    flex-direction: column;
    align-items: center;
    justify-content: center;
    gap: 44px;
    font-family: "Source Sans 3", "Myriad Pro", sans-serif;
  }
  .card {
    position: relative;
    width: 820px;
    height: 530px;
    background: var(--card-black);
    color: var(--gold);
  }
  .gold-rule {
    position: absolute;
    width: 4px;
    background: linear-gradient(180deg, var(--gold-dark), var(--gold-light) 50%, var(--gold-dark));
  }

  /* Vorderseite */
  .card--front .gold-rule--left  { left: 96px;  top: 48px;  height: 220px; }
  .card--front .gold-rule--right { right: 96px; bottom: 48px; height: 220px; }
  .brand {
    position: absolute;
    inset: 0;
    display: flex;
    align-items: center;
    justify-content: center;
    gap: 22px;
  }
  .brand__dot {
    width: 22px;
    height: 22px;
    border-radius: 50%;
    background: var(--gold);
  }
  .brand__name {
    font-size: 64px;
    font-weight: 600;
    letter-spacing: 2px;
    color: var(--gold);
  }

  /* Rückseite */
  .card--back .gold-rule--divider { left: 318px; top: 120px; height: 330px; }
  .contact-brand {
    position: absolute;
    left: 56px;
    top: 120px;
    display: flex;
    align-items: center;
    gap: 10px;
  }
  .contact-brand .brand__dot { width: 12px; height: 12px; }
  .contact-brand .brand__name { font-size: 30px; letter-spacing: 1px; }
  .company {
    position: absolute;
    left: 56px;
    top: 200px;
    margin: 0;
    font-size: 24px;
    line-height: 1.3;
  }
  .address {
    position: absolute;
    left: 356px;
    top: 160px;
    margin: 0;
    font-style: normal;
    font-size: 24px;
    line-height: 1.3;
  }
  .address__block + .address__block { margin-top: 20px; }
  .address p { margin: 0; }
</style>
</head>
<body>
<main class="sheet">

  <section class="card card--front" aria-label="Vorderseite">
    <span class="gold-rule gold-rule--left"></span>
    <div class="brand">
      <span class="brand__dot"></span>
      <span class="brand__name">Aurelia Tafel</span>
    </div>
    <span class="gold-rule gold-rule--right"></span>
  </section>

  <section class="card card--back" aria-label="Rückseite">
    <div class="contact-brand">
      <span class="brand__dot"></span>
      <span class="brand__name">Aurelia Tafel</span>
    </div>
    <p class="company">Musterfirma<br>Ansprechpartner</p>
    <span class="gold-rule gold-rule--divider"></span>
    <address class="address">
      <div class="address__block">
        <p>Kelterweg 14</p>
        <p>65432 Rebenfeld</p>
      </div>
      <div class="address__block">
        <p>06541 - 238470</p>
        <p>hallo@aurelia-tafel.de</p>
        <p>www.tafel-und-genuss.de</p>
      </div>
    </address>
  </section>

</main>
</body>
</html>
```